Power Point Template Kalmora sustainability consulting

Please note:
We are not looking for new design proposals anymore since we've already received templetes from two designers that we really like. We are currently discussing possible changes with them and will make a final decision soon. Thank you very much.

(find english description below)
We are a small German start-up that offers sustainability consulting. For presentations of results, our company presentation, proposals, lectures, etc., we need a PowerPoint template that matches our logo. We come from classic management consulting / strategy consulting and also deal with facts and figures in sustainability consulting. Therefore, the template should not be too fancy and should not only consist of photos. But it shouldn't be a completely sober template either. Our logo with the green leaves for sustainability (three leaves for KALmora) and the white bar chart (with the dynamic swing upwards) reflects our attitude well, where we see ourselves on the range from playful to sober and classic to modern.

It might be nice for the template to include the shape of one of the leaves (from the logo). Also, the logo should appear in a corner of each slide. The colors from the logo (see appendix) should be partially reflected in the presentation. We can also imagine a gold-brown tone (see website www.kalmora-consulting.example) or a coral tone as a contrast. (Attention - the website is not final yet).

For a first suggestion, it is sufficient to suggest three to four slides (cover sheet, chapter/separation slide, text slide, data slide). We will then mark drafts that we like. In total, we would then need about 6-10 more slide templates, e.g. about us, team, slide for a statement, 2-3 data charts (pie, bar, column), top 3 - 5 list, timeline, contact (more slides are welcome ).

We are a small German start-up offering sustainability consulting. We need a power point template for result presentations, our company presentation, proposals, lectures etc. The template should be aligned with our logo. Our background lies in classic management consulting / strategy consulting and we also deal with facts and figures in sustainability consulting. Therefore, the template should not be too playful and not only consist of photos. But it should also not be a completely clear template. Our logo with the green leaves for sustainability (three leaves for KALmora) and the white bar chart (with the dynamic upward swing) reflects our attitude well, where we see ourselves on the range from playful to down-to-earth and classic to modern .

For the template, it might be nice to incorporate the shape of one of the leaves (from the logo). Also, the logo should show up in one corner on each slide. Some of the colors from the logo (see attachment) should be reflected in the presentation. We could also think of a gold-brown tone (see website www.kalmora-consulting.example) or a coral tone for contrast. (Attention - the website is not final yet).

For a first proposal it is quite sufficient to suggest us three to four slides (cover page, chapter/separation slide, text slide, data slide). We will then mark the drafts that we like. In total we would need about 6-10 more slide templates, eg About us, Team, slide for a statement, 2-3 data charts (pie, bar, column), Top 3 - 5 List, Timeline, Contact (more slides are welcome).

Target Market(s)

Corporations, large companies and SMEs

Industry/Entity Type

Unternehmensberatung, Nachhaltigkeitsberatung

Font styles to use
Sans Serif
Other font styles liked:
• Calibri

Colors
00AB8E
00BBA5
67D7C9
C6EFE9
E9F9F6

Requirements
Must have
• see description (e.g. the colors of our logo)
Nice to have
• see description (e.g. elements of the logo included)
Should not have
• see description

```html
<!DOCTYPE html>
<html lang="en">
<head>
<meta charset="utf-8">
<title>Kalmora Consulting – Presentation Template Overview</title>
<link href="https://fonts.googleapis.com/css2?family=Jost:wght@300;400;500&display=swap" rel="stylesheet">
<style>
:root{
  --paper:#ffffff;
  --canvas:#ffffff;
  --gold:#c09a62;
  --gold-soft:#d9c29c;
  --green:#4d7a1c;
  --green-dark:#3a5a12;
  --green-mid:#6f9a2c;
  --green-light:#a9c64a;
  --green-pale:#e3edc7;
  --grey:#6a6d6e;
  --grey-dark:#505354;
  --text:#7b7b7b;
  --line:#e6dccb;
}
*{margin:0;padding:0;box-sizing:border-box}
html,body{width:1200px;height:1200px;overflow:hidden;background:var(--canvas)}
body{font-family:'Jost',sans-serif;font-weight:300;color:var(--text)}
.deck{position:absolute;left:35px;top:60px;display:grid;grid-template-columns:repeat(4,258px);grid-auto-rows:145px;column-gap:32.5px;row-gap:41.7px}
.slide{position:relative;width:258px;height:145px;background:var(--paper);overflow:hidden;box-shadow:0 3px 8px rgba(0,0,0,.13)}
.slide > *{position:absolute}
/* side strip */
.side{left:0;top:0;bottom:0;width:14px;border-right:.5px solid var(--line)}
.side.r{left:auto;right:0;border-right:0;border-left:.5px solid var(--line)}
.side .dot{position:absolute;left:3.5px;top:4px;width:7px;height:7px;border-radius:50%;background:var(--green-light)}
.side .nm{position:absolute;left:0;right:0;top:12px;text-align:center;font-size:2.3px;color:var(--green);font-weight:400}
.side .url{position:absolute;left:4px;bottom:24px;writing-mode:vertical-rl;transform:rotate(180deg);font-size:2.3px;color:var(--green)}
.side .num{position:absolute;left:0;bottom:0;width:14px;height:12px;background:var(--gold-soft);color:#fff;font-size:2.6px;display:flex;align-items:center;justify-content:center}
/* type */
.kicker{font-size:2.3px;color:var(--grey)}
.h{font-size:5.6px;color:var(--gold);line-height:1.2;font-weight:300}
.hc{font-size:7.4px;color:var(--gold);text-align:center;left:14px;right:0;font-weight:300}
.tx{font-size:2.3px;line-height:1.5;color:var(--text)}
.tx.j{text-align:justify}
.tx.gold{color:var(--gold-soft)}
.sub{font-size:2.6px;color:var(--gold-soft)}
.bar-note{border-left:.6px solid var(--grey-dark);padding-left:3px}
.foot{right:10px;bottom:4px;font-size:2.4px;color:var(--grey)}
.foot b{font-weight:400;color:var(--gold)}
/* photo placeholders */
.ph{display:block}
.forest{background:radial-gradient(ellipse at 30% 20%,rgba(235,240,225,.75),rgba(235,240,225,0) 55%),linear-gradient(160deg,#7f9a86,#4f6e5c 55%,#6d8a63)}
.office{background:linear-gradient(135deg,#eef0f1,#b9bec2 55%,#6f757a)}
.paper{background:linear-gradient(150deg,#dfe3e5,#f4f4f2 45%,#8d9498)}
.people{background:linear-gradient(90deg,#8e9194,#3e4145 35%,#6b6e72 65%,#3b3e42)}
.mount{background:linear-gradient(180deg,#e4e2c9,#a9b597 45%,#5f7655)}
.apple{background:radial-gradient(circle at 60% 70%,#8bb03a,#4d6e2e 40%,#2e4a2a)}
.beige{background:linear-gradient(100deg,#a99872,#c7b892 55%,#d8cdb0)}
.face{background:radial-gradient(circle at 50% 45%,#d8b49a,#a57e66 55%,#5d4a40)}
/* icons */
.ico{width:11px;height:11px;border-radius:50%;background:var(--green-mid);display:flex;align-items:center;justify-content:center}
.ico svg{width:6px;height:6px}
.feat{width:58px;text-align:center}
.feat .lbl{font-size:2.7px;color:var(--gold-soft);margin-top:3px}
.brand-word{font-weight:300;color:var(--grey-dark)}
.topic{background:var(--green-pale);color:var(--gold);font-size:4.3px;text-align:center;line-height:1.15;display:flex;align-items:center;justify-content:center}
.bul li{list-style:none;position:relative;padding-left:3px;margin-bottom:1.5px}
.bul li::before{content:"";position:absolute;left:0;top:.8px;width:1.2px;height:1.2px;background:var(--gold);border-radius:50%}
</style>
</head>
<body>
<main class="deck">

<!-- 1 cover -->
<section class="slide">
  <div class="ph beige" role="img" aria-label="Warm sepia photo of a consultant in an office" style="left:0;top:13px;width:244px;height:118px"></div>
  <span style="left:44px;top:52px;width:10px;height:10px;border-radius:50%;background:var(--green)"></span>
  <div class="brand-word" style="left:19px;top:64px;font-size:16px">Kalmora</div>
  <div style="left:40px;top:83px;font-size:3px;color:var(--grey-dark);letter-spacing:.2px">CONSULTING</div>
  <div style="left:106px;top:28px;font-size:11.5px;line-height:1.1;color:#fff">PLACE HERE YOUR<br>TITLE<br>PRESENTATION</div>
  <div style="left:106px;top:84px;font-size:3.6px;color:#f3eee2">Your Subtitle Presentation goes here</div>
  <div style="left:106px;top:101px;font-size:2.2px;color:#f3eee2;line-height:1.5">Presented by: Name Surname, Managing Partner<br>Presented on: 01 Jan 2025</div>
  <div class="foot">Visit us | www.kalmora-consulting.example</div>
</section>

<!-- 2 welcome -->
<section class="slide">
  <span style="left:17px;top:14px;width:8px;height:8px;border-radius:50%;background:var(--green)"></span>
  <div class="brand-word" style="left:28px;top:11px;font-size:9px">Kalmora</div>
  <div style="left:52px;top:23px;font-size:2px;color:var(--grey)">CONSULTING</div>
  <div class="h" style="left:17px;top:70px;font-size:9px">Welcome,</div>
  <div style="left:17px;top:89px;font-size:4.3px;color:var(--grey-dark);line-height:3.1">Lorem Ipsum is simply dummy text of the printing<br>and typesetting industry.</div>
  <span style="left:168px;top:30px;width:62px;height:62px;border-radius:50%;background:var(--green-light);opacity:.85"></span>
  <div style="left:172px;top:96px;font-size:13px;color:var(--green)">Kalmora</div>
  <div style="left:6px;bottom:4px;font-size:2.4px;color:var(--grey)">2</div>
  <div class="foot">Visit us | www.kalmora-consulting.example</div>
</section>

<!-- 3 table of content -->
<section class="slide">
  <div class="side r"><span class="dot"></span><span class="nm">Kalmora</span><span class="url">www.kalmora-consulting.example</span><span class="num">3</span></div>
  <div class="kicker" style="left:32px;top:22px">Welcome</div>
  <div class="h" style="left:32px;top:26px">Table of Content</div>
  <div class="tx bar-note" style="left:32px;top:42px;width:175px">Lorem Ipsum is simply dummy text of the printing and typesetting industry. Lorem Ipsum has been the industry's standard dummy text ever since the 1500s, when a printer took a galley of type.</div>
  <div class="tx" style="left:32px;top:64px;width:42px"><span class="sub">About Us</span><br>01.1 What About Us<br>01.2 Our Team<br>01.3 Facts</div>
  <div class="tx" style="left:91px;top:64px;width:42px"><span class="sub">Section two description</span><br>02.1 What is the Method?<br>02.2 What we do<br>02.3 Certified</div>
  <div class="tx" style="left:150px;top:64px;width:42px"><span class="sub">Section three description</span><br>03.1 What is Kalmora?<br>03.2 Why Us<br>03.3 Our experience</div>
  <div class="tx" style="left:32px;top:93px;width:42px"><span class="sub">Section Four description</span><br>04.1 Introduction<br>04.2 Corporate Colors<br>04.3 Color Scheme</div>
  <div class="tx" style="left:91px;top:93px;width:42px"><span class="sub">Section Five description</span><br>05.1 Print System<br>05.2 Web System<br>05.3 Corporate Images</div>
  <div class="tx" style="left:150px;top:93px;width:42px"><span class="sub">Section Six description</span><br>06.1 Introduction<br>06.2 Icon Application<br>06.3 Infographic System</div>
</section>

<!-- 4 company intro -->
<section class="slide">
  <div class="side r"><span class="dot"></span><span class="nm">Kalmora</span><span class="url">www.kalmora-consulting.example</span><span class="num">4</span></div>
  <div class="ph people" role="img" aria-label="Photo of three consultants in dark suits" style="left:13px;top:19px;width:137px;height:103px"></div>
  <div class="kicker" style="left:162px;top:27px">Company Introduction</div>
  <div class="h" style="left:162px;top:31px">Our Company Intro</div>
  <div style="left:162px;top:39px;font-size:3px;color:var(--gold)">Welcome to the best Company.</div>
  <div class="tx gold" style="left:162px;top:49px;width:74px">Lorem Ipsum is simply dummy text of the printing and typesetting industry. Lorem Ipsum has been the industry's standard dummy text ever since the 1500s, when an unknown printer took a galley of type and scrambled it to make a type specimen book. It has survived not only five centuries, but also the leap into electronic typesetting, remaining essentially unchanged.</div>
  <span style="left:200px;top:112px;width:34px;height:.5px;background:var(--gold-soft)"></span>
</section>

<!-- 5 brand guidelines -->
<section class="slide">
  <div class="side"><span class="dot"></span><span class="nm">Kalmora</span><span class="url">www.kalmora-consulting.example</span><span class="num">5</span></div>
  <div class="kicker" style="left:31px;top:24px">Brand Guideline Introduction</div>
  <div class="h" style="left:31px;top:29px">Our Brand Guidelines</div>
  <div class="tx bar-note" style="left:31px;top:48px;width:95px">Lorem Ipsum is simply dummy text of the printing and typesetting industry. Lorem Ipsum has been the industry's standard dummy text ever since the 1500s, when a printer took a galley of type.</div>
  <div class="ico" style="left:36px;top:83px;width:13px;height:13px"><svg viewBox="0 0 10 10"><path d="M2 8 L7 3 L8 4 L3 9 Z" fill="#fff"/></svg></div>
  <div class="ico" style="left:95px;top:83px;width:13px;height:13px"><svg viewBox="0 0 10 10"><rect x="2.5" y="1.5" width="5" height="7" fill="none" stroke="#fff" stroke-width="1"/></svg></div>
  <div class="tx" style="left:31px;top:102px;width:42px"><span class="sub">Your subtitle slide here</span><br>Lorem Ipsum is simply dummy text of the printing and typesetting industry.</div>
  <div class="tx" style="left:91px;top:102px;width:42px"><span class="sub">Your subtitle slide here</span><br>Lorem Ipsum is simply dummy text of the printing and typesetting industry.</div>
  <div class="ph forest" role="img" aria-label="Photo of sunlight in a green forest" style="left:150px;top:13px;width:94px;height:118px"></div>
</section>

<!-- 6 branding values -->
<section class="slide">
  <div class="side r"><span class="dot"></span><span class="nm">Kalmora</span><span class="url">www.kalmora-consulting.example</span><span class="num">6</span></div>
  <div class="ph paper" role="img" aria-label="Photo of a hand writing in a notebook" style="left:13px;top:13px;width:69px;height:87px"></div>
  <div class="ph office" role="img" aria-label="Photo of a businesswoman working on a laptop" style="left:89px;top:13px;width:69px;height:87px"></div>
  <div class="tx" style="left:16px;top:106px;width:63px">Lorem Ipsum is simply dummy text of the printing and typesetting industry. Lorem Ipsum has been the standard dummy text ever since.</div>
  <div class="tx" style="left:92px;top:106px;width:63px">Lorem Ipsum is simply dummy text of the printing and typesetting industry. Lorem Ipsum has been the standard dummy text ever since.</div>
  <div class="kicker" style="left:166px;top:19px">Lorem Ipsum is simply dummy text of the</div>
  <div class="h" style="left:166px;top:24px">Branding Values and<br>Reputation</div>
  <div class="sub" style="left:166px;top:42px">Lorem Ipsum is simply dummy text</div>
  <div class="tx" style="left:166px;top:50px;width:68px">Lorem Ipsum is simply dummy text of the printing and typesetting industry. Lorem Ipsum has been the industry's standard dummy text ever since the 1500s, when an unknown printer took a galley of type and scrambled it to make a type specimen book. It has survived not only five centuries, but also the leap into electronic typesetting.</div>
  <div class="tx gold" style="left:166px;top:99px;width:68px">Lorem Ipsum is simply dummy text of the printing and typesetting industry.</div>
  <span style="left:166px;top:127px;width:66px;height:1.5px;background:var(--green-mid)"></span>
</section>

<!-- 7 company values -->
<section class="slide">
  <div class="side"><span class="dot"></span><span class="nm">Kalmora</span><span class="url">www.kalmora-consulting.example</span><span class="num">7</span></div>
  <div class="kicker" style="left:31px;top:23px">Company Values</div>
  <div class="h" style="left:31px;top:28px">Company Values and<br>Strengths</div>
  <div class="tx gold j" style="left:31px;top:47px;width:74px">Lorem Ipsum is simply dummy text of the printing and typesetting industry. Lorem Ipsum has been the standard dummy text ever since the 1500s, when a printer took a galley of type.</div>
  <div class="tx j" style="left:31px;top:73px;width:74px">When an unknown printer took a galley of type and scrambled it to make a type specimen book. It has survived not only five centuries, but also the leap into electronic typesetting, remaining essentially unchanged. It was popularised in the 1960s with the release of sheets containing Lorem Ipsum passages, and more recently with desktop publishing software including versions of Lorem Ipsum.</div>
  <div class="sub" style="left:128px;top:22px">Our Identity</div>
  <div class="sub" style="left:168px;top:22px">Our Values</div>
  <div class="sub" style="left:207px;top:22px">Our Philosophy</div>
  <div class="ph people" role="img" aria-label="Photo of the consulting team" style="left:128px;top:28px;width:35px;height:27px"></div>
  <div class="ph office" role="img" aria-label="Photo of a meeting at a desk" style="left:168px;top:28px;width:35px;height:27px"></div>
  <div class="ph paper" role="img" aria-label="Photo of hands with documents" style="left:207px;top:28px;width:35px;height:27px"></div>
  <div class="tx" style="left:128px;top:61px;width:34px">Lorem Ipsum is simply dummy text of the printing and typesetting industry. Lorem Ipsum has been the industry's standard dummy text ever since the 1500s.</div>
  <div class="tx" style="left:168px;top:61px;width:34px">Lorem Ipsum is simply dummy text of the printing and typesetting industry. Lorem Ipsum has been the industry's standard dummy text ever since the 1500s.</div>
  <div class="tx" style="left:207px;top:61px;width:34px">Lorem Ipsum is simply dummy text of the printing and typesetting industry. Lorem Ipsum has been the industry's standard dummy text ever since the 1500s.</div>
</section>

<!-- 8 section break -->
<section class="slide">
  <div class="ph forest" role="img" aria-label="Photo of sunbeams through a green forest" style="left:0;top:0;width:258px;height:145px"></div>
  <svg style="left:0;top:0" width="258" height="145" viewBox="0 0 258 145"><path d="M0 145 C70 110 150 118 258 118 L258 145 Z" fill="#fff"/></svg>
  <div style="left:0;right:0;top:68px;text-align:center;font-size:13px;color:#fff">BRAKE SECTION SLIDE</div>
  <div style="left:0;right:0;top:91px;text-align:center;font-size:3.6px;color:#fff">Lorem Ipsum is simply dummy text of the printing and typesetting</div>
  <span style="left:188px;top:130px;width:5px;height:5px;border-radius:50%;background:var(--green)"></span>
  <div class="brand-word" style="left:195px;top:127px;font-size:6px">Kalmora</div>
</section>

<!-- 9 about products -->
<section class="slide">
  <div class="side"><span class="dot"></span><span class="nm">Kalmora</span><span class="url">www.kalmora-consulting.example</span><span class="num">9</span></div>
  <div class="kicker" style="left:32px;top:14px">Lorem Ipsum is simply dummy</div>
  <div class="h" style="left:32px;top:24px">About Our Products</div>
  <div class="ph paper" role="img" aria-label="Photo of a hand pointing at an open notebook" style="left:32px;top:39px;width:100px;height:66px"></div>
  <div class="tx" style="left:156px;top:38px;width:75px"><span class="sub">Your subtitle slide here</span><br>Lorem Ipsum is simply dummy text of the printing and typesetting industry. Lorem Ipsum has been the industry's standard dummy text ever since the 1500s.</div>
  <div class="tx" style="left:156px;top:62px;width:75px"><span class="sub">Your subtitle slide here</span><br>Lorem Ipsum is simply dummy text of the printing and typesetting industry. Lorem Ipsum has been the industry's standard dummy text ever since the 1500s.</div>
  <div class="tx" style="left:156px;top:86px;width:75px"><span class="sub">Your subtitle slide here</span><br>Lorem Ipsum is simply dummy text of the printing and typesetting industry. Lorem Ipsum has been the industry's standard dummy text ever since the 1500s.</div>
  <div class="tx" style="left:32px;top:110px;width:206px"><span class="sub">Your subtitle slide here</span><br>When an unknown printer took a galley of type and scrambled it to make a type specimen book. It has survived not only five centuries, but also the leap into electronic typesetting, remaining essentially unchanged. It was popularised in the 1960s with the release of sheets containing passages, and more recently with desktop publishing software.</div>
</section>

<!-- 10 section break -->
<section class="slide">
  <div class="ph" role="img" aria-label="Photo of a misty forest landscape with green leaves" style="left:0;top:0;width:258px;height:145px;background:linear-gradient(100deg,#e6dcc2,#b9b99a 30%,#5f7d66 55%,#3f5f47 80%,#76915a)"></div>
  <span style="left:24px;top:20px;width:12px;height:12px;border-radius:50%;background:var(--green-mid)"></span>
  <div style="left:38px;top:21px;font-size:6px;color:var(--green)">Kalmora</div>
  <div style="left:0;right:0;top:68px;text-align:center;font-size:13px;color:#fff">BRAKE SECTION SLIDE</div>
</section>

<!-- 11 bullets -->
<section class="slide">
  <div class="side"><span class="dot"></span><span class="nm">Kalmora</span><span class="url">www.kalmora-consulting.example</span><span class="num">11</span></div>
  <div class="hc" style="top:11px;font-size:5.6px">Click here to your title Bullets slide</div>
  <div class="feat" style="left:25px;top:33px"><div class="ico" style="margin:0 auto"><svg viewBox="0 0 10 10"><circle cx="5" cy="4.2" r="2.6" fill="none" stroke="#fff"/><path d="M4 7.5h2" stroke="#fff"/></svg></div><div class="lbl">Consultancy</div><div class="tx">Lorem ipsum randomised words which don't look even slightly believable in some form.</div></div>
  <div class="feat" style="left:102px;top:33px"><div class="ico" style="margin:0 auto"><svg viewBox="0 0 10 10"><circle cx="5" cy="5" r="3.3" fill="none" stroke="#fff"/><path d="M5 3v2.2l1.4.9" stroke="#fff" fill="none"/></svg></div><div class="lbl">Consultancy</div><div class="tx">Lorem ipsum randomised words which don't look even slightly believable in some form.</div></div>
  <div class="feat" style="left:179px;top:33px"><div class="ico" style="margin:0 auto"><svg viewBox="0 0 10 10"><circle cx="4.3" cy="4.3" r="2.4" fill="none" stroke="#fff"/><path d="M6 6l2.3 2.3" stroke="#fff"/></svg></div><div class="lbl">Consultancy</div><div class="tx">Lorem ipsum randomised words which don't look even slightly believable in some form.</div></div>
  <div class="feat" style="left:25px;top:83px"><div class="ico" style="margin:0 auto"><svg viewBox="0 0 10 10"><circle cx="5" cy="5" r="3.3" fill="none" stroke="#fff"/><circle cx="5" cy="5" r="1.3" fill="#fff"/></svg></div><div class="lbl">Consultancy</div><div class="tx">Lorem ipsum randomised words which don't look even slightly believable in some form.</div></div>
  <div class="feat" style="left:102px;top:83px"><div class="ico" style="margin:0 auto"><svg viewBox="0 0 10 10"><path d="M5 9C3 6.5 2.3 5.3 2.3 4A2.7 2.7 0 0 1 7.7 4C7.7 5.3 7 6.5 5 9Z" fill="none" stroke="#fff"/><circle cx="5" cy="4" r="1" fill="#fff"/></svg></div><div class="lbl">Consultancy</div><div class="tx">Lorem ipsum randomised words which don't look even slightly believable in some form.</div></div>
  <div class="feat" style="left:179px;top:83px"><div class="ico" style="margin:0 auto"><svg viewBox="0 0 10 10"><circle cx="5" cy="3.4" r="1.7" fill="#fff"/><path d="M1.8 8.8a3.2 3 0 0 1 6.4 0Z" fill="#fff"/></svg></div><div class="lbl">Consultancy</div><div class="tx">Lorem ipsum randomised words which don't look even slightly believable in some form.</div></div>
</section>

<!-- 12 team -->
<section class="slide">
  <div class="side"><span class="dot"></span><span class="nm">Kalmora</span><span class="url">www.kalmora-consulting.example</span><span class="num">12</span></div>
  <div class="hc" style="top:11px;font-size:6.2px">Meet our Team</div>
  <div class="ph face" role="img" aria-label="Portrait photo of a partner" style="left:44px;top:43px;width:31px;height:31px;border-radius:50%"></div>
  <div class="ph face" role="img" aria-label="Portrait photo of a partner" style="left:119px;top:43px;width:31px;height:31px;border-radius:50%"></div>
  <div class="ph face" role="img" aria-label="Portrait photo of a partner" style="left:194px;top:43px;width:31px;height:31px;border-radius:50%"></div>
  <div class="tx" style="left:35px;top:80px;width:48px;text-align:center"><span class="sub">Partner name</span><br>Job position here</div>
  <div class="tx" style="left:110px;top:80px;width:48px;text-align:center"><span class="sub">Partner name</span><br>Job position here</div>
  <div class="tx" style="left:185px;top:80px;width:48px;text-align:center"><span class="sub">Partner name</span><br>Job position here</div>
  <div class="tx j" style="left:38px;top:94px;width:43px">When an unknown printer took a galley of type and scrambled it to make a type specimen book. It has survived not only five centuries, but also the leap into typesetting.</div>
  <div class="tx j" style="left:113px;top:94px;width:43px">When an unknown printer took a galley of type and scrambled it to make a type specimen book. It has survived not only five centuries, but also the leap into typesetting.</div>
  <div class="tx j" style="left:188px;top:94px;width:43px">When an unknown printer took a galley of type and scrambled it to make a type specimen book. It has survived not only five centuries, but also the leap into typesetting.</div>
</section>

<!-- 13 product background -->
<section class="slide">
  <div class="side"><span class="dot"></span><span class="nm">Kalmora</span><span class="url">www.kalmora-consulting.example</span><span class="num">13</span></div>
  <div class="kicker" style="left:32px;top:24px">Lorem Ipsum is simply dummy text</div>
  <div class="h" style="left:32px;top:29px">How our Product Works Background</div>
  <div class="tx" style="left:32px;top:42px;width:128px">Lorem Ipsum is simply dummy text of the printing and typesetting industry. Lorem Ipsum has been the industry's standard dummy text ever since the 1500s, when an unknown printer took a galley of type and scrambled it to make a type specimen book. It has survived not only five centuries, but also the leap into electronic typesetting, remaining essentially unchanged. It was popularised in the 1960s with the release of sheets containing passages.</div>
  <div class="tx" style="left:32px;top:78px;width:128px">We want to see more charts translating our vision of having a market leading platform, digitalise in the space to provide 360 degree content.</div>
  <span style="left:32px;top:96px;width:6px;height:6px;border-radius:50%;background:var(--green-mid)"></span>
  <span style="left:72px;top:96px;width:6px;height:6px;border-radius:50%;background:var(--green-mid)"></span>
  <span style="left:112px;top:96px;width:6px;height:6px;border-radius:50%;background:var(--green-mid)"></span>
  <div class="tx" style="left:40px;top:96px;width:27px">Lorem Ipsum is simply dummy text of the printing and typesetting industry. Lorem Ipsum has been the standard text ever since the 1500s.</div>
  <div class="tx" style="left:80px;top:96px;width:27px">Lorem Ipsum is simply dummy text of the printing and typesetting industry. Lorem Ipsum has been the standard text ever since the 1500s.</div>
  <div class="tx" style="left:120px;top:96px;width:27px">Lorem Ipsum is simply dummy text of the printing and typesetting industry. Lorem Ipsum has been the standard text ever since the 1500s.</div>
  <div class="ph mount" role="img" aria-label="Photo of misty green mountains" style="left:170px;top:0;width:74px;height:38px"></div>
  <div class="ph forest" role="img" aria-label="Photo of sunlight in a forest" style="left:170px;top:41px;width:74px;height:43px"></div>
  <div class="ph apple" role="img" aria-label="Photo of green apples on a branch" style="left:170px;top:87px;width:74px;height:58px"></div>
</section>

<!-- 14 product background 2 -->
<section class="slide">
  <div class="side"><span class="dot"></span><span class="nm">Kalmora</span><span class="url">www.kalmora-consulting.example</span><span class="num">14</span></div>
  <div class="kicker" style="left:31px;top:19px">Lorem Ipsum is simply dummy text</div>
  <div class="h" style="left:31px;top:24px">How our Product<br>Works Background</div>
  <div class="tx j" style="left:31px;top:42px;width:95px">Lorem Ipsum is simply dummy text of the printing and typesetting industry. Lorem Ipsum has been the industry's standard dummy text ever since the 1500s, when an unknown printer took a galley of type and scrambled it to make a type specimen book. It has survived not only five centuries, but also the leap into electronic typesetting, remaining essentially unchanged. It was popularised in the 1960s with the release of sheets containing passages, and more recently with desktop publishing software.</div>
  <div class="tx j" style="left:31px;top:79px;width:95px">When an unknown printer took a galley of type and scrambled it to make a type specimen book. It has survived not only five centuries, but also the leap into electronic typesetting, remaining essentially unchanged. It was popularised in the 1960s with the release of sheets containing passages. It has survived not only five centuries, but also the leap into electronic typesetting, remaining essentially unchanged, and more recently with desktop publishing software including versions of Lorem Ipsum.</div>
  <div class="ph paper" role="img" aria-label="Photo of a hand writing notes on paper" style="left:141px;top:20px;width:103px;height:51px"></div>
  <div class="ph office" role="img" aria-label="Photo of two consultants at a laptop" style="left:141px;top:75px;width:103px;height:51px"></div>
</section>

<!-- 15 text and three images -->
<section class="slide">
  <div class="side"><span class="dot"></span><span class="nm">Kalmora</span><span class="url">www.kalmora-consulting.example</span><span class="num">15</span></div>
  <span style="left:30px;top:24px;width:76px;height:.8px;background:var(--green-mid)"></span>
  <div class="kicker" style="left:31px;top:31px">Image System</div>
  <div class="h" style="left:31px;top:36px">Text Slide &amp; Three Images</div>
  <div class="tx j" style="left:31px;top:50px;width:92px">Lorem Ipsum is simply dummy text of the printing and typesetting industry. Lorem Ipsum has been the industry's standard dummy text ever since the 1500s, when an unknown printer took a galley of type and scrambled it to make a type specimen book. It has survived not only five centuries, but also the leap into electronic typesetting, remaining essentially unchanged. It was popularised in the 1960s with the release of sheets, and more recently with desktop publishing software including versions of Lorem Ipsum.</div>
  <div class="sub" style="left:31px;top:108px">Lorem Ipsum is simply dummy text of the printing</div>
  <div class="tx" style="left:31px;top:113px;width:92px">Typesetting When an unknown printer took a galley of type and scrambled it to make a type specimen book. It has survived not only five centuries.</div>
  <div class="ph office" role="img" aria-label="Photo of a businesswoman smiling" style="left:131px;top:24px;width:54px;height:107px"></div>
  <div class="ph apple" role="img" aria-label="Photo of green apples on a tree" style="left:190px;top:24px;width:55px;height:50px"></div>
  <div class="ph mount" role="img" aria-label="Photo of hazy mountains" style="left:190px;top:79px;width:55px;height:52px"></div>
</section>

<!-- 16 three columns with images -->
<section class="slide">
  <div class="side"><span class="dot"></span><span class="nm">Kalmora</span><span class="url">www.kalmora-consulting.example</span><span class="num">16</span></div>
  <div class="hc" style="top:14px;font-size:7px">Click to edit title slide</div>
  <div class="hc" style="top:28px;font-size:1.9px;color:var(--gold-soft);letter-spacing:.1px">LOREM IPSUM USING INFORMATION ON ITS ORIGINS, AS WELL AS A RANDOM TEXT HERE</div>
  <div style="left:25px;top:46px;width:63px;text-align:center;font-size:4.3px;color:var(--gold)">Lorem dummy text</div>
  <div style="left:98px;top:46px;width:63px;text-align:center;font-size:4.3px;color:var(--gold)">Lorem dummy text</div>
  <div style="left:172px;top:46px;width:63px;text-align:center;font-size:4.3px;color:var(--gold)">Lorem dummy text</div>
  <div class="ph mount" role="img" aria-label="Photo of green hills" style="left:25px;top:57px;width:63px;height:37px"></div>
  <div class="ph paper" role="img" aria-label="Photo of hands with a notebook" style="left:98px;top:57px;width:63px;height:37px"></div>
  <div class="ph office" role="img" aria-label="Photo of a business meeting" style="left:172px;top:57px;width:63px;height:37px"></div>
  <div style="left:25px;top:99px;width:63px;font-size:2.9px;line-height:1.55;color:var(--grey)">Lorem Ipsum is simply dummy text of the printing and typesetting industry. Lorem Ipsum has been the.</div>
  <div style="left:98px;top:99px;width:63px;font-size:2.9px;line-height:1.55;color:var(--grey)">Lorem Ipsum is simply dummy text of the printing and typesetting industry. Lorem Ipsum has been the.</div>
  <div style="left:172px;top:99px;width:63px;font-size:2.9px;line-height:1.55;color:var(--grey)">Lorem Ipsum is simply dummy text of the printing and typesetting industry. Lorem Ipsum has been the.</div>
</section>

<!-- 17 feature timeline -->
<section class="slide">
  <div class="side"><span class="dot"></span><span class="nm">Kalmora</span><span class="url">www.kalmora-consulting.example</span><span class="num">17</span></div>
  <div class="hc" style="top:18px">Your Title Text Goes Here</div>
  <svg style="left:0;top:0" width="258" height="145" viewBox="0 0 258 145">
    <path d="M14 110 C22 70 50 62 73 85 C85 108 98 108 110 85 C122 62 136 62 148 85 C160 108 173 108 185 85 C197 62 215 62 222 85 C232 112 250 100 258 78" fill="none" stroke="#d6d6d6" stroke-width=".6"/>
    <g fill="#fff" stroke="#e2e2e2" stroke-width="1.2">
      <circle cx="73" cy="85" r="12"/><circle cx="110" cy="85" r="12"/><circle cx="148" cy="85" r="12"/><circle cx="185" cy="85" r="12"/>
    </g>
    <g fill="none" stroke="#8fb040" stroke-width="1.2">
      <path d="M61 85 A12 12 0 0 0 85 85"/><path d="M98 85 A12 12 0 0 1 110 73"/><path d="M136 85 A12 12 0 0 0 160 85"/><path d="M185 73 A12 12 0 0 1 197 85"/>
    </g>
    <g fill="none" stroke="#6f9a2c" stroke-width=".7">
      <rect x="68" y="80" width="9" height="7"/><path d="M71 90h4"/>
      <circle cx="110" cy="82" r="2.2"/><path d="M106 90a4 3 0 0 1 8 0"/>
      <circle cx="148" cy="85" r="4"/><path d="M148 82.5v2.5l1.6 1"/>
      <path d="M181 89l8-8M183 81h6v6"/>
    </g>
    <g font-size="2.3" fill="#c9c9c9" font-family="Jost, sans-serif"><text x="69" y="101">1990</text><text x="106" y="70">2005</text><text x="144" y="101">2020</text><text x="181" y="70">2030</text></g>
  </svg>
  <div class="tx" style="left:53px;top:48px;width:40px;text-align:center"><span style="color:var(--grey-dark)">Feature title one</span><br>Lorem ipsum dolor sit amet, consectetuer</div>
  <div class="tx" style="left:128px;top:48px;width:40px;text-align:center"><span style="color:var(--grey-dark)">Feature title one</span><br>Lorem ipsum dolor sit amet, consectetuer</div>
  <div class="tx" style="left:90px;top:106px;width:40px;text-align:center"><span style="color:var(--grey-dark)">Feature title one</span><br>Lorem ipsum dolor sit amet, consectetuer</div>
  <div class="tx" style="left:165px;top:106px;width:40px;text-align:center"><span style="color:var(--grey-dark)">Feature title one</span><br>Lorem ipsum dolor sit amet, consectetuer</div>
</section>

<!-- 18 year timeline -->
<section class="slide">
  <div class="side"><span class="dot"></span><span class="nm">Kalmora</span><span class="url">www.kalmora-consulting.example</span><span class="num">18</span></div>
  <div class="hc" style="top:18px">Your Title Text Goes Here</div>
  <div class="tx" style="left:44px;top:35px;width:186px;text-align:center;font-size:2.6px">Lorem ipsum dolor sit amet, consectetuer adipiscing elit. Aenean commodo ligula eget dolor. Aenean massa. Cum sociis natoque penatibus et magnis dis parturient montes, nascetur ridiculus mus.</div>
  <svg style="left:0;top:0" width="258" height="145" viewBox="0 0 258 145">
    <g fill="#fff" stroke-width="3.4">
      <circle cx="50" cy="87" r="15" stroke="#3a5a12"/>
      <circle cx="84" cy="87" r="15" stroke="#4d7a1c"/>
      <circle cx="117" cy="87" r="15" stroke="#6f9a2c"/>
      <circle cx="151" cy="87" r="15" stroke="#a9c64a"/>
      <circle cx="184" cy="87" r="15" stroke="#6a6d6e"/>
      <circle cx="218" cy="87" r="15" stroke="#505354"/>
    </g>
    <g font-size="7" fill="#505354" text-anchor="middle" font-family="Jost, sans-serif" font-weight="300">
      <text x="50" y="89.5">1992</text><text x="84" y="89.5">1995</text><text x="117" y="89.5">2000</text><text x="151" y="89.5">2007</text><text x="184" y="89.5">2016</text><text x="218" y="89.5">2022</text>
    </g>
  </svg>
  <div class="tx" style="left:35px;top:59px;width:30px;text-align:center">Amazing history content</div>
  <div class="tx" style="left:102px;top:59px;width:30px;text-align:center">Amazing history content</div>
  <div class="tx" style="left:169px;top:59px;width:30px;text-align:center">Amazing history content</div>
  <div class="tx" style="left:69px;top:110px;width:30px;text-align:center">Amazing history content</div>
  <div class="tx" style="left:136px;top:110px;width:30px;text-align:center">Amazing history content</div>
  <div class="tx" style="left:203px;top:110px;width:30px;text-align:center">Amazing history content</div>
</section>

<!-- 19 two column text -->
<section class="slide">
  <div class="side"><span class="dot"></span><span class="nm">Kalmora</span><span class="url">www.kalmora-consulting.example</span><span class="num">19</span></div>
  <div class="hc" style="top:11px">Two Column Text Slide</div>
  <ul class="tx j bul" style="left:20px;top:26px;width:108px;height:114px;overflow:hidden">
    <li>Lorem ipsum dolor sit amet, consectetur adipiscing elit. Nulla sit amet urna sagittis, maximus orci eget, sodales nibh. Duis eu purus gravida, dignissim eros posuere, ornare nisi. Pellentesque habitant morbi tristique senectus et netus et malesuada fames ac turpis egestas. Fusce quam ex, commodo vitae pellentesque sit amet, tempor sodales purus. Cras convallis vestibulum urna nec convallis. Fusce eu auctor odio. Sed sagittis, libero ut pretium mollis, est eros maximus quam, nec ultrices ex diam eget ipsum.</li>
    <li>Suspendisse in sollicitudin mauris, in commodo dui. Aenean ut dui aliquam, elementum dolor vitae, commodo ex. Phasellus commodo enim ut fringilla commodo. Nulla porttitor erat at lacus interdum, et dictum enim sagittis. Morbi vel lacus sed dui elementum elementum in at turpis. Aenean maximus ornare dui et ultricies. Nam lacus arcu, ullamcorper vel pretium ac, placerat efficitur ipsum. Nullam non vestibulum quam.</li>
    <li>Duis venenatis tristique lacus non porttitor. Aenean elit justo, molestie vel pretium nec, fringilla vitae augue. Etiam purus leo, faucibus ac varius in, tempor vel ex. Morbi pulvinar porttitor mauris, at tincidunt massa.</li>
  </ul>
  <ul class="tx j bul" style="left:133px;top:26px;width:108px;height:114px;overflow:hidden">
    <li>Lorem ipsum dolor sit amet, consectetur adipiscing elit. Nulla sit amet urna sagittis, maximus orci eget, sodales nibh. Duis eu purus gravida, dignissim eros posuere, ornare nisi. Pellentesque habitant morbi tristique senectus et netus et malesuada fames ac turpis egestas. Fusce quam ex, commodo vitae pellentesque sit amet, tempor sodales purus. Cras convallis vestibulum urna nec convallis. Fusce eu auctor odio. Sed sagittis, libero ut pretium mollis, est eros maximus quam, nec ultrices ex diam eget ipsum.</li>
    <li>Suspendisse in sollicitudin mauris, in commodo dui. Aenean ut dui aliquam, elementum dolor vitae, commodo ex. Phasellus commodo enim ut fringilla commodo. Nulla porttitor erat at lacus interdum, et dictum enim sagittis. Morbi vel lacus sed dui elementum elementum in at turpis. Aenean maximus ornare dui et ultricies. Nam lacus arcu, ullamcorper vel pretium ac, placerat efficitur ipsum. Nullam non vestibulum quam.</li>
    <li>Duis venenatis tristique lacus non porttitor. Aenean elit justo, molestie vel pretium nec, fringilla vitae augue. Etiam purus leo, faucibus ac varius in, tempor vel ex. Morbi pulvinar porttitor mauris, at tincidunt massa.</li>
  </ul>
</section>

<!-- 20 two topics -->
<section class="slide">
  <div class="side"><span class="dot"></span><span class="nm">Kalmora</span><span class="url">www.kalmora-consulting.example</span><span class="num">20</span></div>
  <div class="hc" style="top:7px">Two Topics Text Slide</div>
  <div class="topic" style="left:18px;top:22px;width:110px;height:18px">Lorem ipsum dolor sit amet,<br>consectetur adipiscing elit</div>
  <div class="topic" style="left:131px;top:22px;width:110px;height:18px">Lorem ipsum dolor sit amet,<br>consectetur adipiscing elit</div>
  <ul class="tx j bul" style="left:20px;top:46px;width:106px;height:94px;overflow:hidden">
    <li>Lorem ipsum dolor sit amet, consectetur adipiscing elit. Nulla sit amet urna sagittis, maximus orci eget, sodales nibh. Duis eu purus gravida, dignissim eros posuere, ornare nisi. Pellentesque habitant morbi tristique senectus et netus et malesuada fames ac turpis egestas. Fusce quam ex, commodo vitae pellentesque sit amet, tempor sodales purus. Cras convallis vestibulum urna nec convallis. Fusce eu auctor odio. Sed sagittis, libero ut pretium mollis, est eros maximus quam, nec ultrices ex diam eget ipsum.</li>
    <li>Suspendisse in sollicitudin mauris, in commodo dui. Aenean ut dui aliquam, elementum dolor vitae, commodo ex. Phasellus commodo enim ut fringilla commodo. Nulla porttitor erat at lacus interdum, et dictum enim sagittis. Morbi vel lacus sed dui elementum elementum in at turpis. Aenean maximus ornare dui et ultricies. Nam lacus arcu, ullamcorper vel pretium ac, placerat efficitur ipsum.</li>
  </ul>
  <ul class="tx j bul" style="left:133px;top:46px;width:106px;height:94px;overflow:hidden">
    <li>Lorem ipsum dolor sit amet, consectetur adipiscing elit. Nulla sit amet urna sagittis, maximus orci eget, sodales nibh. Duis eu purus gravida, dignissim eros posuere, ornare nisi. Pellentesque habitant morbi tristique senectus et netus et malesuada fames ac turpis egestas. Fusce quam ex, commodo vitae pellentesque sit amet, tempor sodales purus. Cras convallis vestibulum urna nec convallis. Fusce eu auctor odio. Sed sagittis, libero ut pretium mollis, est eros maximus quam, nec ultrices ex diam eget ipsum.</li>
    <li>Suspendisse in sollicitudin mauris, in commodo dui. Aenean ut dui aliquam, elementum dolor vitae, commodo ex. Phasellus commodo enim ut fringilla commodo. Nulla porttitor erat at lacus interdum, et dictum enim sagittis. Morbi vel lacus sed dui elementum elementum in at turpis. Aenean maximus ornare dui et ultricies. Nam lacus arcu, ullamcorper vel pretium ac, placerat efficitur ipsum.</li>
  </ul>
</section>

<!-- 21 column chart -->
<section class="slide">
  <div class="side"><span class="dot"></span><span class="nm">Kalmora</span><span class="url">www.kalmora-consulting.example</span><span class="num">21</span></div>
  <div class="h" style="left:18px;top:25px">Click to include your title<br>slide for data analysis</div>
  <ul class="tx bul" style="left:20px;top:44px;width:80px">
    <li>Lorem ipsum dolor sit amet, consectetur adipiscing elit. Nulla sit amet urna sagittis, maximus orci eget, sodales nibh.</li>
    <li>Duis eu purus gravida, dignissim eros posuere, ornare nisi. Pellentesque habitant morbi tristique senectus et netus et malesuada fames ac turpis egestas.</li>
    <li>Fusce quam ex, commodo vitae pellentesque sit amet, tempor sodales purus. Cras convallis vestibulum urna nec convallis.</li>
    <li>Fusce eu auctor odio. Sed sagittis, libero ut pretium mollis, est eros maximus quam, nec ultrices ex diam eget ipsum.</li>
  </ul>
  <svg style="left:0;top:0" width="258" height="145" viewBox="0 0 258 145">
    <text x="175" y="28" font-size="3.2" fill="#6a6d6e" text-anchor="middle" font-family="Jost, sans-serif">Chart Title</text>
    <g stroke="#eee" stroke-width=".3"><path d="M110 36h134M110 56h134M110 76h134M110 96h134"/></g>
    <path d="M110 116h134" stroke="#ccc" stroke-width=".4"/>
    <g fill="#4d7a1c"><rect x="118" y="55" width="5" height="61"/><rect x="148" y="76" width="5" height="40"/><rect x="178" y="66" width="5" height="50"/><rect x="208" y="52" width="5" height="64"/></g>
    <g fill="#6a6d6e"><rect x="124" y="75" width="5" height="41"/><rect x="154" y="49" width="5" height="67"/><rect x="184" y="89" width="5" height="27"/><rect x="214" y="75" width="5" height="41"/></g>
    <g fill="#6f9a2c"><rect x="130" y="85" width="5" height="31"/><rect x="160" y="85" width="5" height="31"/><rect x="190" y="72" width="5" height="44"/><rect x="220" y="46" width="5" height="70"/></g>
    <g font-size="2" fill="#999" text-anchor="middle" font-family="Jost, sans-serif"><text x="127" y="120">Category 1</text><text x="157" y="120">Category 2</text><text x="187" y="120">Category 3</text><text x="217" y="120">Category 4</text><text x="175" y="125">■ Series 1  ■ Series 2  ■ Series 3</text></g>
  </svg>
</section>

<!-- 22 pie chart -->
<section class="slide">
  <div class="side"><span class="dot"></span><span class="nm">Kalmora</span><span class="url">www.kalmora-consulting.example</span><span class="num">22</span></div>
  <div class="h" style="left:18px;top:25px">Click to include your title<br>slide for data analysis</div>
  <ul class="tx bul" style="left:20px;top:44px;width:80px">
    <li>Lorem ipsum dolor sit amet, consectetur adipiscing elit. Nulla sit amet urna sagittis, maximus orci eget, sodales nibh.</li>
    <li>Duis eu purus gravida, dignissim eros posuere, ornare nisi. Pellentesque habitant morbi tristique senectus et netus et malesuada fames ac turpis egestas.</li>
    <li>Fusce quam ex, commodo vitae pellentesque sit amet, tempor sodales purus. Cras convallis vestibulum urna nec convallis.</li>
    <li>Fusce eu auctor odio. Sed sagittis, libero ut pretium mollis, est eros maximus quam, nec ultrices ex diam eget ipsum.</li>
  </ul>
  <svg style="left:0;top:0" width="258" height="145" viewBox="0 0 258 145">
    <text x="175" y="27" font-size="3.2" fill="#6a6d6e" text-anchor="middle" font-family="Jost, sans-serif">Sales</text>
    <path d="M113 61 v8 A62 31 0 0 0 237 69 v-8 Z" fill="#2f4a0e"/>
    <path d="M175 61 L175 30 A62 31 0 1 1 126 80 Z" fill="#3a5a12"/>
    <path d="M175 61 L126 80 A62 31 0 0 1 128 41 Z" fill="#5c5f61"/>
    <path d="M175 61 L128 41 A62 31 0 0 1 150 32.5 Z" fill="#a9c64a"/>
    <path d="M175 61 L150 32.5 A62 31 0 0 1 175 30 Z" fill="#8fb040"/>
    <g font-size="2" fill="#999" text-anchor="middle" font-family="Jost, sans-serif"><text x="175" y="121">■ 1st Qtr  ■ 2nd Qtr  ■ 3rd Qtr  ■ 4th Qtr</text></g>
  </svg>
</section>

<!-- 23 bar chart -->
<section class="slide">
  <div class="side"><span class="dot"></span><span class="nm">Kalmora</span><span class="url">www.kalmora-consulting.example</span><span class="num">23</span></div>
  <div class="h" style="left:18px;top:25px">Click to include your title<br>slide for data analysis</div>
  <ul class="tx bul" style="left:20px;top:44px;width:80px">
    <li>Lorem ipsum dolor sit amet, consectetur adipiscing elit. Nulla sit amet urna sagittis, maximus orci eget, sodales nibh.</li>
    <li>Duis eu purus gravida, dignissim eros posuere, ornare nisi. Pellentesque habitant morbi tristique senectus et netus et malesuada fames ac turpis egestas.</li>
    <li>Fusce quam ex, commodo vitae pellentesque sit amet, tempor sodales purus. Cras convallis vestibulum urna nec convallis.</li>
    <li>Fusce eu auctor odio. Sed sagittis, libero ut pretium mollis, est eros maximus quam, nec ultrices ex diam eget ipsum.</li>
  </ul>
  <svg style="left:0;top:0" width="258" height="145" viewBox="0 0 258 145">
    <text x="175" y="27" font-size="3.2" fill="#6a6d6e" text-anchor="middle" font-family="Jost, sans-serif">Sales</text>
    <path d="M122 36v76" stroke="#ccc" stroke-width=".4"/>
    <g fill="#3f6a12"><rect x="122" y="38" width="15" height="9"/><rect x="122" y="59" width="18" height="9"/><rect x="122" y="80" width="41" height="9"/><rect x="122" y="101" width="107" height="9"/></g>
    <g font-size="2" fill="#999" font-family="Jost, sans-serif" text-anchor="end"><text x="120" y="43">4th Qtr</text><text x="120" y="64">3rd Qtr</text><text x="120" y="85">2nd Qtr</text><text x="120" y="106">1st Qtr</text></g>
    <g font-size="1.8" fill="#aaa" font-family="Jost, sans-serif"><text x="122" y="116">0</text><text x="141" y="116">1</text><text x="160" y="116">2</text><text x="179" y="116">3</text><text x="198" y="116">4</text><text x="217" y="116">5</text><text x="236" y="116">6</text></g>
    <text x="175" y="122" font-size="2" fill="#999" text-anchor="middle" font-family="Jost, sans-serif">■ 1st Qtr  ■ 2nd Qtr  ■ 3rd Qtr  ■ 4th Qtr</text>
  </svg>
</section>

<!-- 24 thank you -->
<section class="slide">
  <div class="ph" role="img" aria-label="Sepia photo of misty mountain ridges" style="left:0;top:13px;width:244px;height:118px;background:linear-gradient(180deg,#b49a6c,#c9b287 45%,#dccbab 75%,#cdb994)"></div>
  <div style="left:27px;top:43px;font-size:11px;color:#fff">THANK YOU.</div>
  <div style="left:27px;top:59px;font-size:3px;color:#f5efe2">Kalmora Consulting GmbH</div>
  <span style="left:27px;top:66px;width:73px;height:.7px;background:var(--green-mid)"></span>
  <div style="left:27px;top:70px;font-size:2.4px;line-height:1.55;color:#f5efe2">Kalmora Consulting GmbH<br>Example Street 12<br>00000 Sample City<br>Tel. +00 000 0000000<br>E-Mail: hello@kalmora-consulting.example</div>
  <div class="foot">Visit us | www.kalmora-consulting.example</div>
</section>

</main>
</body>
</html>
```